BIX Promotional flyer for students

We're looking for an 8.5" x 11" flyer that will be distributed to schools. Please see language to include in attached files.

Target Market(s)

The parents and teachers of high school students

Industry/Entity Type

Mental health

Other font styles liked:
• Monserrat and Roboto Slab

Requirements
Must have
• See attached pdf for language to be included on the flyer. Please use the color palette from our website: www.bixzone.tv. Please include some imagery of students. Please ensure the
Nice to have
• Feel free to use any of the graphics provided. See our website for our brand look & feel: www.bixzone.tv

```html
<!DOCTYPE html>
<html lang="en">
<head>
<meta charset="utf-8">
<title>Fundraise with BIX</title>
<link rel="stylesheet" href="https://fonts.googleapis.com/css2?family=Montserrat:ital,wght@0,600;0,700;0,800;0,900;1,500&display=swap">
<style>
  :root {
    --orange: #ff7410;
    --orange-deep: #ff5e1b;
    --peach: #ffbe8c;
    --blue: #2271b3;
    --sky: #69bfd9;
    --navy: #05348a;
    --ink: #0e1010;
    --cream: #fdf8f4;
    --white: #ffffff;
  }
  * { margin: 0; padding: 0; box-sizing: border-box; }
  html, body { width: 927px; height: 1200px; overflow: hidden; background: var(--orange); }
  .flyer {
    position: relative;
    width: 927px; height: 1200px;
    overflow: hidden;
    background: var(--orange);
    font-family: "Montserrat", sans-serif;
  }
  .shapes { position: absolute; inset: 0; }
  .headline-fundraise {
    position: absolute; left: 86px; top: 70px;
    font-size: 74px; font-weight: 700; letter-spacing: 6px;
    color: var(--white); line-height: 1;
  }
  .headline-with {
    position: absolute; right: 338px; top: 151px;
    font-size: 37px; font-weight: 800; letter-spacing: 2px;
    color: var(--white); line-height: 1;
  }
  .brand-mark {
    position: absolute;
    color: var(--white); font-weight: 800; line-height: 1;
    text-align: center; letter-spacing: -2px;
  }
  .brand-mark.top { left: 621px; top: 98px; width: 208px; font-size: 84px; }
  .brand-mark.bottom { left: 61px; top: 981px; width: 170px; font-size: 66px; }
  .proceeds { position: absolute; left: 89px; top: 292px; width: 356px; text-align: center; }
  .proceeds-figure { font-size: 108px; font-weight: 900; color: var(--blue); line-height: 1; letter-spacing: -4px; }
  .proceeds-label { font-size: 21px; font-weight: 800; color: var(--orange); margin-top: 10px; }
  .proceeds-return { font-size: 30px; font-weight: 800; color: var(--blue); line-height: 1.05; margin-top: 12px; letter-spacing: -0.5px; }
  .mission {
    position: absolute; left: 72px; top: 610px;
    font-size: 55px; font-weight: 800; color: var(--white);
    line-height: 63px; letter-spacing: 1px;
  }
  .about {
    position: absolute; left: 193px; top: 978px; width: 362px;
    font-size: 16px; font-style: italic; font-weight: 500;
    color: var(--ink); line-height: 30.5px; text-align: center; letter-spacing: 0.3px;
  }
  .web {
    position: absolute; left: 645px; top: 1104px;
    font-size: 29px; font-weight: 800; color: var(--orange); letter-spacing: 0.5px;
  }
</style>
</head>
<body>
<div class="flyer">
  <svg class="shapes" width="927" height="1200" viewBox="0 0 927 1200">
    <defs>
      <radialGradient id="portraitTone" cx="0.72" cy="0.5" r="0.6">
        <stop offset="0" stop-color="#b0583a"/>
        <stop offset="0.45" stop-color="#5a2c1e"/>
        <stop offset="1" stop-color="#0e1010"/>
      </radialGradient>
    </defs>
    <!-- top right corner -->
    <path d="M530 0 H927 V60 Q700 40 620 120 Z" fill="var(--peach)"/>
    <circle cx="725" cy="47" r="104" fill="var(--blue)"/>
    <circle cx="862" cy="181" r="148" fill="var(--sky)"/>
    <!-- portrait area -->
    <polygon role="img" aria-label="Portrait photo of a young man looking at the camera"
      points="621,220 927,220 927,1200 371,1200 371,540 456,400" fill="url(#portraitTone)"/>
    <circle cx="862" cy="181" r="148" fill="var(--sky)"/>
    <circle cx="725" cy="136" r="104" fill="var(--orange-deep)" stroke="var(--white)" stroke-width="2"/>
    <!-- proceeds bubble -->
    <circle cx="176" cy="330" r="153" fill="var(--blue)"/>
    <circle cx="262" cy="372" r="190" fill="var(--orange)" stroke="var(--orange)" stroke-width="2"/>
    <circle cx="266" cy="372" r="188" fill="none" stroke="var(--orange)" stroke-width="4"/>
    <circle cx="275" cy="382" r="182" fill="var(--white)"/>
    <circle cx="265" cy="380" r="180" fill="var(--white)" stroke="var(--orange)" stroke-width="3"/>
    <!-- mission panel -->
    <polygon points="40,590 464,590 622,746 622,876 40,876" fill="none" stroke="var(--orange)" stroke-width="3"/>
    <polygon points="46,592 464,592 618,747 618,870 46,870" fill="#141211" fill-opacity="0.94"/>
    <!-- bottom left cluster -->
    <circle cx="40" cy="880" r="102" fill="var(--blue)"/>
    <circle cx="181" cy="1010" r="150" fill="var(--sky)"/>
    <path d="M34 980 Q60 880 145 870 Q140 960 80 982 Z" fill="var(--navy)"/>
    <!-- about bubble -->
    <circle cx="378" cy="1097" r="200" fill="none" stroke="var(--orange)" stroke-width="3"/>
    <circle cx="373" cy="1116" r="212" fill="var(--cream)"/>
    <path d="M176 1116 A200 200 0 0 1 300 913" fill="none" stroke="var(--orange)" stroke-width="3"/>
    <circle cx="146" cy="1013" r="86" fill="var(--orange-deep)" stroke="var(--white)" stroke-width="2"/>
  </svg>

  <div class="headline-fundraise">FUNDRAISE</div>
  <div class="headline-with">WITH</div>
  <div class="brand-mark top">bix</div>

  <div class="proceeds">
    <div class="proceeds-figure">50%</div>
    <div class="proceeds-label">OF ALL PROCEEDS</div>
    <div class="proceeds-return">GO BACK TO<br>YOUR SCHOOL</div>
  </div>

  <h1 class="mission">SUPPORT<br>THE MENTAL<br>HEALTH OF<br>YOUR STUDENTS</h1>

  <div class="brand-mark bottom">bix</div>
  <p class="about">is a simple and effective way<br>to improve mental health. Your<br>students will learn valuable<br>coping skills and techniques from<br>expert clinicians who analyze real cases<br>and share their insights and advice.</p>

  <div class="web">BIXZONE.TV</div>
</div>
</body>
</html>
```